OpenCart website

We have an existing site that was based on open cart in 2011 but customised heavily. We want a brand new open cart site designed from scratch so we can work on transitioning the existing opencart database over after the project is done

Current site: www.quillfernstores.com

```html
<!DOCTYPE html>
<html lang="en">
<head>
<meta charset="utf-8">
<title>Quillfern Stores</title>
<link href="https://fonts.googleapis.com/css2?family=Source+Sans+3:wght@400;600;700&display=swap" rel="stylesheet">
<style>
:root{
  --red:#e8262b;
  --ink:#222;
  --muted:#666;
  --panel:#eceff3;
  --cream:#f8f2e0;
  --dark:#1e1e1e;
  --line:#e4e4e4;
}
*{box-sizing:border-box;margin:0;padding:0}
html,body{width:1200px;height:1200px;overflow:hidden;background:#fff}
body{font-family:"Source Sans 3",sans-serif;color:var(--ink)}
.stage{position:relative;width:1500px;height:1500px;transform:scale(.8);transform-origin:0 0}
.abs{position:absolute}
.topbar{left:456px;top:0;width:590px;height:17px;background:#eef0f3;font-size:5px;color:#555;text-align:right;padding:6px 74px 0 0}
.logo{left:530px;top:27px;font-weight:700;font-size:13px;color:var(--red);line-height:11px}
.logo span{display:block;color:var(--ink);font-size:9px}
.search{left:652px;top:28px;width:196px;height:16px;border:1px solid var(--line);font-size:4.5px;color:#999;padding:5px 6px}
.search-btn{left:850px;top:28px;width:44px;height:16px;background:var(--red);color:#fff;font-size:5px;text-align:center;line-height:16px}
.nav{left:456px;top:55px;width:590px;height:20px;background:#222;display:flex;gap:18px;padding-left:74px;align-items:center;font-size:5px;color:#fff}
.cats{left:530px;top:80px;width:93px;height:188px;border:1px solid var(--line)}
.cats-head{height:16px;background:var(--red);color:#fff;font-size:5.5px;line-height:16px;padding-left:8px}
.cats ul{list-style:none;padding-top:5px}
.cats li{height:11.4px;font-size:4.5px;line-height:11.4px;padding-left:8px;color:#555}
.cats li:nth-child(even){background:#eef0f4}
.hero{left:630px;top:80px;width:226px;height:188px;background:var(--cream)}
.ph{background:linear-gradient(135deg,#e34a2e,#6fb36a 60%,#2b4e9a)}
.hero h1{position:absolute;left:10px;top:110px;font-size:12px;font-weight:700;letter-spacing:.3px}
.hero p{position:absolute;left:10px;top:128px;font-size:4.7px;color:#555}
.btn-out{position:absolute;border:1px solid var(--red);color:var(--red);font-size:4.5px;text-align:center}
.promo{left:862px;width:110px;height:90px;background:#e6e9ee}
.promo h3{position:absolute;left:8px;top:10px;font-size:9px;font-weight:700}
.promo h3 em{font-style:normal;color:var(--red);font-size:8px;font-weight:600}
.feature{top:296px;width:144px;height:51px;display:flex;align-items:center;padding-left:16px;gap:12px}
.feature b{display:block;font-size:5.5px}
.feature small{font-size:4.2px;color:#555}
.ico{width:20px;height:20px;border-radius:50%;background:rgba(0,0,0,.08);display:flex;align-items:center;justify-content:center}
.sec-title{left:456px;width:590px;top:389px;text-align:center;font-size:12px;font-weight:600}
.arrow{width:12px;height:12px;border:1px solid var(--line);font-size:7px;text-align:center;line-height:10px;background:#fff}
.card{top:430px;width:106px;height:168px;border:1px solid var(--line)}
.card .img{position:absolute;left:7px;top:6px;width:91px;height:108px;background:var(--panel)}
.card .img i{position:absolute;left:10px;right:10px;top:28px;bottom:24px;border-radius:4px}
.card h4{position:absolute;left:8px;top:123px;font-size:5.5px;font-weight:600}
.card p{position:absolute;left:8px;top:134px;font-size:4.5px;color:#666;line-height:7.5px}
.brand{top:666px;height:16px;font-size:7px;font-weight:600;color:#555;line-height:16px;letter-spacing:.5px}
.tile{background:var(--panel)}
.tile h5{position:absolute;left:10px;top:18px;font-size:6.5px;font-weight:600;letter-spacing:.2px}
.tile .art{position:absolute;left:18px;right:18px;top:40px;bottom:12px;border-radius:6px}
.sale-photo{background:linear-gradient(160deg,#5b5f63,#8a8580 50%,#7a4a55)}
.sale-text{left:530px;width:139px;top:817px;text-align:center;color:#fff;font-weight:700}
.testi p{position:absolute;left:10px;right:10px;top:30px;font-size:4.5px;line-height:11.5px;text-align:center;color:#444}
.footer{left:456px;top:1278px;width:590px;height:222px;background:var(--dark);color:#bbb}
.fcol{position:absolute;top:45px;font-size:4.5px;line-height:13.4px}
.fcol b{display:block;color:#fff;font-size:5.5px;font-weight:700;margin-bottom:1px}
.pay{top:46px;font-size:6.5px;font-weight:700;color:#bbb}
.social{top:99px;width:18px;height:18px;background:#fff}
</style>
</head>
<body>
<div class="stage">

  <div class="abs topbar">Become a New Customer &nbsp;|&nbsp; Credit Application &amp; Prepaid Shipping &nbsp;|&nbsp; Download Credit Application</div>

  <div class="abs logo">QUILLFERN<span>STORES</span></div>
  <div class="abs search">Search Over 4,000 Products...</div>
  <div class="abs search-btn">SEARCH</div>
  <svg class="abs" style="left:926px;top:29px" width="15" height="15" viewBox="0 0 15 15" fill="none" stroke="#555" stroke-width="1"><circle cx="7.5" cy="7.5" r="6.8"/><circle cx="7.5" cy="6" r="2.3"/><path d="M3.3 12c1-2 2.5-3 4.2-3s3.2 1 4.2 3"/></svg>
  <svg class="abs" style="left:955px;top:29px" width="16" height="15" viewBox="0 0 16 15" fill="none" stroke="#555" stroke-width="1"><path d="M1.5 4.5h9l-1 9h-7z"/><path d="M4 4.5V3a2 2 0 0 1 4 0v1.5"/><circle cx="13" cy="3" r="2.6" fill="#222" stroke="none"/></svg>

  <nav class="abs nav"><span>HOME</span><span>ABOUT US</span><span>MY ACCOUNT</span><span>MY SHOPPING LIST</span><span>LOCATION &amp; CONTACTS</span><span>SITE MAP</span></nav>

  <aside class="abs cats">
    <div class="cats-head">&#9776;&nbsp; ALL CATEGORIES</div>
    <ul>
      <li>Cleaning Supplies</li><li>Cookware And Baking</li><li>Crafts And Hobbies</li><li>Food</li><li>Glassware</li><li>Hardware</li><li>Health And Beauty</li><li>Home Accessories</li><li>Kitchenware</li><li>Plasticware</li><li>Seasonal</li><li>Stainless Steel</li><li>Tableware</li><li>Opportunity Buys</li>
    </ul>
  </aside>

  <section class="abs hero">
    <div class="abs ph" role="img" aria-label="Red baking dish and colourful food container set" style="left:12px;top:18px;width:160px;height:72px;border-radius:4px"></div>
    <h1>FOOD CONTAINERS</h1>
    <p>Vivamus id dolor nunc. Vivamus vehicula nisl elementum sollicitudin finibus.</p>
    <div class="btn-out" style="left:12px;top:145px;width:40px;height:12px;line-height:10px">Learn More</div>
  </section>

  <div class="abs promo" style="top:80px">
    <h3>SALE <em>20% OFF</em></h3>
    <div class="abs" role="img" aria-label="Blue enamel coffee pots and cookware" style="left:6px;top:38px;width:98px;height:48px;border-radius:4px;background:linear-gradient(135deg,#2a4aa0,#1c2c6a)"></div>
  </div>
  <div class="abs promo" style="top:178px;background:#fff;border:1px solid var(--line)">
    <h3 style="font-size:7.5px;top:14px">NEW <em style="font-size:7.5px">ARRIVALS</em></h3>
    <div class="abs" role="img" aria-label="Amber glass decanter set with gift box" style="left:6px;top:30px;width:96px;height:56px;border-radius:4px;background:linear-gradient(135deg,#e0a030,#f3e6d2)"></div>
  </div>

  <div class="abs feature" style="left:530px;background:#dff8fb">
    <span class="ico"><svg width="11" height="8" viewBox="0 0 11 8" fill="none" stroke="#333" stroke-width=".8"><rect x=".5" y=".5" width="6" height="5"/><path d="M6.5 2.5h2.5l1.5 1.5v1.5h-4"/><circle cx="2.5" cy="6.5" r="1"/><circle cx="8.5" cy="6.5" r="1"/></svg></span>
    <div><b>FREE SHIPPING</b><small>On orders over $ 99</small></div>
  </div>
  <div class="abs feature" style="left:679px;background:#d9dadb">
    <span class="ico"><svg width="10" height="10" viewBox="0 0 10 10" fill="none" stroke="#333" stroke-width=".9"><path d="M2 3a3.8 3.8 0 1 1-.6 3"/><path d="M1.5 1v2.3h2.3"/></svg></span>
    <div><b>ORDER RETURN</b><small>Returns within 7 days</small></div>
  </div>
  <div class="abs feature" style="left:828px;background:#c8e2f7">
    <span class="ico"><svg width="11" height="8" viewBox="0 0 11 8" fill="none" stroke="#333" stroke-width=".8"><rect x=".5" y=".5" width="10" height="7"/><path d="M.5 .5l5 4 5-4"/></svg></span>
    <div><b>CONTACT US</b><small>Contact us for support services</small></div>
  </div>

  <h2 class="abs sec-title">New Arrivals</h2>
  <div class="abs" style="left:727px;top:407px;width:46px;height:1.5px;background:var(--red)"></div>
  <div class="abs arrow" style="left:937px;top:404px">&#8249;</div>
  <div class="abs arrow" style="left:959px;top:404px">&#8250;</div>

  <div class="abs card" style="left:530px"><div class="img"><i role="img" aria-label="Sport squeeze bottles in four colours" style="background:linear-gradient(90deg,#d33,#2a8a3a,#c13a8a,#2a5ac0)"></i></div><h4>Bottle Sport Soft Grip 22oz</h4><p>Item No: 072517<br>Inner Pack: 0<br>Case Pack: 36</p></div>
  <div class="abs card" style="left:642px"><div class="img"><i role="img" aria-label="Insulated travel mugs in red and blue" style="background:linear-gradient(90deg,#7a2040,#2040a0)"></i></div><h4>Bottle Sport Soft Grip 22oz</h4><p>Item No: 072517<br>Inner Pack: 0<br>Case Pack: 36</p></div>
  <div class="abs card" style="left:755px"><div class="img"><i role="img" aria-label="Mixing bowl and kitchen utensil set" style="background:linear-gradient(90deg,#c8ccd2,#d8323a)"></i></div><h4>Bottle Sport Soft Grip 22oz</h4><p>Item No: 072517<br>Inner Pack: 0<br>Case Pack: 36</p></div>
  <div class="abs card" style="left:867px"><div class="img"><i role="img" aria-label="Boxed citrus juicers in red and green" style="background:linear-gradient(90deg,#c8323a,#6cbf40)"></i></div><h4>Bottle Sport Soft Grip 22oz</h4><p>Item No: 072517<br>Inner Pack: 0<br>Case Pack: 36</p></div>

  <div class="abs arrow" style="left:530px;top:667px">&#8249;</div>
  <div class="abs brand" style="left:566px">VANTRO</div>
  <div class="abs brand" style="left:619px">PELHAM</div>
  <div class="abs brand" style="left:670px">KELBY</div>
  <div class="abs brand" style="left:724px">NORVANE</div>
  <div class="abs brand" style="left:781px">BRIXA</div>
  <div class="abs brand" style="left:840px">OSTRIA</div>
  <div class="abs brand" style="left:902px">TOLMER</div>
  <div class="abs arrow" style="left:959px;top:667px">&#8250;</div>

  <div class="abs sale-photo" role="img" aria-label="Glass storage jars on a woven cloth" style="left:530px;top:731px;width:139px;height:212px"></div>
  <div class="abs sale-text" style="font-size:18px">SALE</div>
  <div class="abs sale-text" style="top:843px;font-size:12px">20% OFF</div>
  <div class="abs" style="left:580px;top:866px;width:39px;height:11px;background:var(--red);color:#fff;font-size:4.5px;text-align:center;line-height:11px">Learn More</div>

  <div class="abs tile" style="left:530px;top:955px;width:139px;height:140px"><h5>SUSPENDISSE ACCUMSAN</h5><div class="art" role="img" aria-label="Patterned ceramic bowls" style="background:linear-gradient(135deg,#c9604a,#2e3550)"></div></div>
  <div class="abs tile" style="left:530px;top:1106px;width:139px;height:140px"><h5>SUSPENDISSE ACCUMSAN</h5><div class="art" role="img" aria-label="Colourful toy watering cans" style="background:linear-gradient(135deg,#2a7ad0,#7cc63a,#e84a9a)"></div></div>

  <div class="abs tile" style="left:681px;top:731px;width:140px;height:140px"><h5>SUSPENDISSE ACCUMSAN</h5><div class="art" role="img" aria-label="Coloured glass mason jar mugs" style="background:linear-gradient(90deg,#3ab0c8,#6ac02a,#8a40b0,#a0282a)"></div></div>
  <div class="abs tile testi" style="left:681px;top:882px;width:140px;height:212px">
    <p>“Quisque egestas pharetra sagittis. Class aptent sociosqu ad litora torquent per conubia nostra inceptos himenaeos. Donec convallis sit amet purus sed ullamcorper. Suspendisse accumsan rutrum justo aliquam accumsan.”</p>
    <div class="abs" role="img" aria-label="Customer portrait" style="left:43px;top:96px;width:54px;height:54px;border-radius:50%;background:#5a5450;border:2px solid #fff"></div>
    <div class="abs" style="left:0;width:140px;top:157px;text-align:center;font-size:6px;font-weight:600">Marla Quenton</div>
    <div class="abs" style="left:0;width:140px;top:167px;text-align:center;font-size:4.3px;color:#666">Halden</div>
  </div>
  <div class="abs tile" style="left:681px;top:1106px;width:140px;height:140px"><h5>SUSPENDISSE ACCUMSAN</h5><div class="art" role="img" aria-label="Blue mop bucket with wringer" style="background:linear-gradient(135deg,#2a5ad8,#1a3aa0)"></div></div>

  <div class="abs tile" style="left:832px;top:731px;width:140px;height:140px"><h5>SUSPENDISSE ACCUMSAN</h5><div class="art" role="img" aria-label="Nesting rainbow measuring cups" style="background:linear-gradient(135deg,#3a3a3a,#28b0d8,#e84a2a)"></div></div>
  <div class="abs tile" style="left:832px;top:882px;width:140px;height:140px"><h5>SUSPENDISSE ACCUMSAN</h5><div class="art" role="img" aria-label="Cast iron frying pans" style="background:linear-gradient(135deg,#2a2a2a,#555)"></div></div>
  <div class="abs tile" style="left:832px;top:1034px;width:140px;height:212px"><h5>SUSPENDISSE ACCUMSAN</h5><div class="art" role="img" aria-label="Electric salt and pepper grinders" style="background:linear-gradient(90deg,#1c2448,#d82a2a,#9aa0a8)"></div></div>

  <footer class="abs footer">
    <div class="fcol" style="left:77px"><b>HELP</b>Support Center<br>Contact Us<br>Return Policy<br>Shipping<br>Payment Options<br>Discounts<br>100% Guarantee<br>References<br>Buyer Guide<br>Sitemap</div>
    <div class="fcol" style="left:147px"><b>MY ACCOUNT</b>Login / Register<br>Track My Order<br>T&amp;C<br>Privacy</div>
    <div class="fcol" style="left:228px"><b>COMPANY INFO</b>About Us<br>Why Buy From Us<br>FAQ<br>Blog<br>Winners</div>
    <div class="fcol" style="left:309px"><b>PARTNET PROGRAM</b>Affiliates</div>
    <div class="abs pay" style="left:402px">PAYVO</div>
    <div class="abs pay" style="left:437px">CARDMARK</div>
    <div class="abs pay" style="left:482px">SENDWELL</div>
    <div class="abs" style="left:387px;top:68px;width:90px;height:19px;background:#fff;font-size:4.5px;color:#888;padding:7px 6px">E-mail Address</div>
    <div class="abs" style="left:477px;top:68px;width:42px;height:19px;background:var(--red);color:#fff;font-size:5px;text-align:center;line-height:19px">SUBSCRIBE</div>
    <div class="abs social" style="left:427px"></div>
    <div class="abs social" style="left:451px"></div>
    <div class="abs social" style="left:475px"></div>
    <div class="abs social" style="left:499px"></div>
  </footer>

</div>
</body>
</html>
```